Real Estate Website

We currently have an existing site at https://nestorvalley.com.au/ but require a much more professional design.

We like the style/design of the following which are competitors : https://tenzaflow.com.au/
https://www.orvalhaven.com.au/
https://pellowisp.com.au/

```html
<!DOCTYPE html>
<html lang="en">
<head>
<meta charset="utf-8">
<title>Nestor Valley Homes</title>
<link href="https://fonts.googleapis.com/css2?family=Arvo:wght@400;700&family=Poppins:wght@300;400;500&display=swap" rel="stylesheet">
<style>
:root{
  --navy:#1f2a6b;
  --red:#e0353a;
  --text:#555a6e;
  --muted:#8a8f9c;
  --line:#e7e8ec;
  --soft:#f4f4f5;
  --white:#ffffff;
}
*{box-sizing:border-box;margin:0;padding:0}
html,body{width:1200px;height:4085px;overflow:hidden;background:var(--white)}
body{position:relative;font-family:"Poppins",sans-serif;color:var(--text)}
.abs{position:absolute}
.serif{font-family:"Arvo",serif;font-weight:700;color:var(--navy)}
.brand{display:flex;flex-direction:column;align-items:center;gap:8px;font-family:"Poppins",sans-serif;font-weight:500;color:var(--navy);font-size:12px}
.brand .mark{width:30px;height:30px;background:var(--red);border-radius:50%}
.nav{top:78px;right:120px;display:flex;gap:37px;font-size:12px;color:var(--navy)}
.nav .active{color:var(--red)}
.btn{display:flex;align-items:center;justify-content:center;border-radius:30px;font-size:12px;color:var(--navy);background:var(--white);box-shadow:0 6px 18px rgba(0,0,0,.08)}
.btn.red{background:var(--red);color:var(--white);box-shadow:0 6px 14px rgba(224,53,58,.35)}
.center{text-align:center}
.para{font-size:11.5px;line-height:20px}
.card{background:var(--white);box-shadow:0 8px 24px rgba(0,0,0,.08);border-radius:4px;text-align:center}
.card .icon{width:100px;height:96px;margin:40px auto 0;border-radius:8px}
.card h3{font-family:"Arvo",serif;font-weight:700;color:var(--navy);font-size:17px;margin-top:42px}
.card p{font-size:11px;line-height:20px;margin-top:24px;padding:0 50px}
.band{left:0;top:1870px;width:1200px;height:495px;background:var(--red)}
.feat{display:flex;gap:48px;top:2004px;left:310px;font-size:11px;color:var(--white)}
.feat span{display:flex;align-items:center;gap:10px}
.feat i{width:18px;height:18px;background:var(--white);border-radius:3px;display:block}
.calc{left:166px;top:2089px;width:875px;height:396px;background:var(--white);border-radius:24px;box-shadow:0 10px 30px rgba(0,0,0,.08)}
.lbl{font-size:10px;color:var(--muted);text-transform:uppercase}
.field{border:1px solid var(--line);border-radius:22px;height:42px;font-size:11px;color:var(--muted);display:flex;align-items:center;padding:0 20px;box-shadow:0 3px 8px rgba(0,0,0,.04);background:var(--white)}
.field.grey{background:#efefef;border-color:#d6d6d6}
.ring{left:980px;top:1226px;width:554px;height:554px;border-radius:50%;border:135px solid var(--soft)}
.links{font-size:11px;color:var(--text);line-height:25.4px}
.social{display:flex;gap:12px}
.social i{width:11px;height:11px;border-radius:50%;background:var(--red);display:block}
</style>
</head>
<body>

<header>
  <div class="abs brand" style="left:125px;top:55px"><span class="mark"></span>Nestor Valley Homes</div>
  <nav class="abs nav">
    <span class="active">Home</span><span>Sell</span><span>Rent</span><span>Add on Service</span><span>Useful Resources</span><span>About</span>
  </nav>
</header>

<section class="hero">
  <p class="abs" style="left:123px;top:256px;font-size:20px;color:var(--navy)">We help you in</p>
  <h1 class="abs serif" style="left:123px;top:288px;font-size:41px;line-height:51px">Sell and Rent Your<br>Home Yourself</h1>
  <a class="abs btn" style="left:124px;top:415px;width:164px;height:45px">Contact Us</a>
  <a class="abs btn red" style="left:312px;top:415px;width:167px;height:45px">Member Login</a>
  <div class="abs" role="img" aria-label="Photo of an agent meeting a smiling couple on a sofa" style="left:568px;top:171px;width:632px;height:411px;background:linear-gradient(135deg,#d9d4cf,#a6553c 60%,#5c4a44);border-radius:330px 0 0 330px / 411px 0 0 411px"></div>
</section>

<section class="listing">
  <h2 class="abs serif center" style="left:0;width:1200px;top:693px;font-size:23px">Nestor Valley Homes helps you to list on</h2>
  <p class="abs para center" style="left:280px;width:640px;top:748px;font-size:11px">Nestor Valley Homes is an Australia real estate expert who can help you to sell, rent your properties yourself and save thousands of dollars at the same time</p>
  <div class="abs card" style="left:166px;top:864px;width:256px;height:341px">
    <div class="icon" role="img" aria-label="Illustration of a house under a magnifying glass" style="background:linear-gradient(#e66a3a,#2f4a7c)"></div>
    <h3>Sale add on</h3>
    <p>Nestor Valley Homes is an Australia real estate expert who can help you</p>
  </div>
  <div class="abs card" style="left:471px;top:864px;width:256px;height:341px">
    <div class="icon" role="img" aria-label="Illustration of an orange apartment building" style="background:linear-gradient(#f2a23a,#e8792d)"></div>
    <h3>Rental Add on</h3>
    <p>Nestor Valley Homes is an Australia real estate expert who can help you</p>
  </div>
  <div class="abs card" style="left:777px;top:864px;width:256px;height:341px">
    <div class="icon" role="img" aria-label="Illustration of a hanging rent sign" style="background:linear-gradient(#f0c7a0,#7fae3e 45%)"></div>
    <h3>Save by selling</h3>
    <p>Nestor Valley Homes is an Australia real estate expert who can help you</p>
  </div>
</section>

<section class="expert">
  <div class="abs ring"></div>
  <div class="abs" role="img" aria-label="Model house with keys on a grass base" style="left:48px;top:1347px;width:618px;height:420px;background:linear-gradient(160deg,#4d5b7c,#eeeeee 50%,#3f7b3a);border-radius:14px"></div>
  <h2 class="abs serif" style="left:697px;top:1408px;font-size:23px;line-height:31px">Nestor Valley Homes<br>is an Australia real estate expert</h2>
  <p class="abs para" style="left:697px;top:1498px;width:330px;font-size:11px">Nestor Valley Homes is an Australia real estate expert who can help you to sell, rent your properties yourself and save thousands of dollars at the same time</p>
  <a class="abs btn" style="left:697px;top:1612px;width:167px;height:41px;font-size:11px">View More</a>
</section>

<section class="calculator">
  <div class="abs band"></div>
  <h2 class="abs serif center" style="left:0;width:1200px;top:1953px;font-size:23px;color:var(--white)">How much could you save by selling with Nestor Valley Homes?</h2>
  <div class="abs feat"><span><i></i>you are in control</span><span><i></i>easy to use</span><span><i></i>huge savings</span><span><i></i>great support</span></div>
  <div class="abs calc"></div>
  <span class="abs lbl" style="left:228px;top:2129px">Property Value</span>
  <span class="abs lbl" style="left:490px;top:2129px">Agent Commission (%)</span>
  <span class="abs lbl" style="left:755px;top:2129px">Property Value</span>
  <div class="abs field" style="left:219px;top:2149px;width:241px">$ 700000</div>
  <div class="abs field" style="left:485px;top:2149px;width:241px">+ 2.05</div>
  <div class="abs field" style="left:748px;top:2149px;width:241px">+ 5000</div>
  <span class="abs lbl" style="left:228px;top:2213px">Estimated Total Spend With Agent ($)</span>
  <div class="abs field" style="left:219px;top:2229px;width:770px">= 19350</div>
  <span class="abs lbl" style="left:228px;top:2288px">Select Our Package</span>
  <div class="abs field" style="left:219px;top:2308px;width:770px;justify-content:space-between">Basic ($499)<span>⌄</span></div>
  <span class="abs lbl" style="left:228px;top:2372px">Total Saving With Our Package</span>
  <div class="abs field grey" style="left:219px;top:2392px;width:770px">18851</div>
</section>

<section class="testimonial">
  <h2 class="abs serif center" style="left:231px;width:400px;top:2584px;font-size:23px">Testimonials</h2>
  <p class="abs serif center" style="left:231px;width:400px;top:2610px;font-size:64px;color:var(--red)">“</p>
  <p class="abs para center" style="left:261px;width:340px;top:2688px;font-style:italic;font-size:11px">Nestor Valley Homes is an Australia real estate expert who can help you to sell, rent your properties yourself and save thousands of dollars at the same time</p>
  <p class="abs center" style="left:231px;width:400px;top:2776px;font-size:10px"><span class="serif" style="font-size:17px">Jordan</span> &nbsp;- Customer</p>
  <div class="abs" role="img" aria-label="Portrait of a smiling customer" style="left:729px;top:2560px;width:238px;height:238px;border-radius:50%;background:radial-gradient(circle at 50% 45%,#b98466,#4a372e 70%);box-shadow:0 8px 20px rgba(0,0,0,.15);border:6px solid var(--white)"></div>
  <div class="abs" style="left:124px;top:2916px;width:938px;height:1px;background:var(--line)"></div>
</section>

<section class="guide">
  <h2 class="abs serif center" style="left:0;width:1200px;top:3026px;font-size:23px">Free E-Guide for selling/renting your property</h2>
  <div class="abs" style="left:212px;top:3116px;width:351px;height:268px;background:var(--white);box-shadow:0 8px 24px rgba(0,0,0,.1);border-radius:6px">
    <div class="abs" role="img" aria-label="Cover image of a model house" style="left:12px;top:40px;width:205px;height:215px;background:linear-gradient(160deg,#4d5b7c,#eeeeee 50%,#3f7b3a);border-radius:4px"></div>
    <div class="abs" style="left:12px;top:195px;width:110px;height:60px;background:var(--red);border-radius:0 60px 0 0"></div>
    <p class="abs" style="right:30px;top:34px;font-size:6px;color:var(--navy)">Nestor Valley Homes</p>
    <h3 class="abs serif" style="right:30px;top:92px;font-size:16px;line-height:21px;text-align:right">Sell and Rent<br>Your Home<br>Yourself</h3>
    <p class="abs" style="right:30px;top:190px;width:90px;font-size:7px;line-height:11px;text-align:right">Nestor Valley Homes is an Australia real estate expert who can help you to sell,</p>
  </div>
  <div class="abs field" style="left:647px;top:3118px;width:340px">Name</div>
  <div class="abs field" style="left:647px;top:3181px;width:340px">Email</div>
  <div class="abs field" style="left:647px;top:3244px;width:340px;height:75px;align-items:flex-start;padding-top:14px;border-radius:16px">Message</div>
  <a class="abs btn red" style="left:647px;top:3344px;width:340px;height:43px">Send</a>
</section>

<section class="signup">
  <div class="abs" style="left:160px;top:3528px;width:881px;height:162px;background:var(--red);border-radius:6px"></div>
  <div class="abs" role="img" aria-label="Illustration of a woman with a phone beside an envelope and a potted plant" style="left:396px;top:3479px;width:286px;height:230px;background:linear-gradient(180deg,rgba(255,255,255,.0),rgba(255,255,255,.55));border-radius:12px"></div>
  <h2 class="abs serif" style="left:205px;top:3572px;font-size:23px;color:var(--white)">Ready to sign up?</h2>
  <p class="abs" style="left:206px;top:3614px;font-size:10px;line-height:20px;color:var(--white)">Subscribe to our newsletter for the<br>Tenzaflow updates, tips.</p>
  <div class="abs" style="left:680px;top:3587px;width:322px;height:49px;background:var(--white);border-radius:25px;font-size:11px;color:var(--navy);display:flex;align-items:center;padding-left:22px">Email address</div>
  <a class="abs btn" style="left:876px;top:3591px;width:122px;height:41px;background:#111;color:var(--white);font-size:11px">Subscribe</a>
</section>

<footer>
  <div class="abs brand" style="left:198px;top:3750px"><span class="mark"></span>Nestor Valley Homes</div>
  <p class="abs" style="left:198px;top:3832px;width:210px;font-size:10.5px;line-height:20px">Nestor Valley Homes can help you to sell or rent your home yourself with no agent commission.</p>
  <h4 class="abs serif" style="left:480px;top:3760px;font-size:18px">Pages</h4>
  <div class="abs links" style="left:480px;top:3806px">Home<br>Sell<br>Rent<br>Add on Service<br>Useful Resources</div>
  <div class="abs links" style="left:640px;top:3806px">About<br>Contact Us<br>Terms of Use<br>Privacy Policy</div>
  <h4 class="abs serif" style="left:799px;top:3760px;font-size:18px">Contact</h4>
  <div class="abs links" style="left:799px;top:3806px;display:flex;flex-direction:column">
    <span style="display:flex;align-items:center;gap:8px"><svg width="11" height="11" viewBox="0 0 24 24"><path fill="#8a8f9c" d="M6.6 10.8a15 15 0 0 0 6.6 6.6l2.2-2.2a1 1 0 0 1 1-.25 11.4 11.4 0 0 0 3.6.57 1 1 0 0 1 1 1V20a1 1 0 0 1-1 1A17 17 0 0 1 3 4a1 1 0 0 1 1-1h3.5a1 1 0 0 1 1 1c0 1.25.2 2.45.57 3.57a1 1 0 0 1-.25 1z"/></svg>1300 555 014</span>
    <span style="display:flex;align-items:center;gap:8px"><svg width="11" height="9" viewBox="0 0 24 18"><rect width="24" height="18" rx="2" fill="#8a8f9c"/><path d="M1 2l11 8 11-8" stroke="#fff" stroke-width="2" fill="none"/></svg>info@nestorvalley.com.au</span>
  </div>
  <div class="abs social" style="left:799px;top:3886px"><i></i><i></i><i></i></div>
  <div class="abs" style="left:160px;top:3983px;width:881px;height:1px;background:var(--line)"></div>
  <p class="abs center" style="left:0;width:1200px;top:4020px;font-size:10.5px">Copyright @ 2021 Nestor Valley Homes</p>
</footer>

</body>
</html>
```